Penny Harvest

Logo and general packaging design for premium quality, price conscious super foods.

Initial product portfolio includes:

Organic Raw Chia Seeds - Resealable plastic bags with 3 x 5 label.
Organic Cold Pressed Coconut Oil (plastic jar) - 2.5 x 6.5 label

The design should be transferable to additional products.

Project requirements:

The design should be simple and the core trade dress should be no more than 2 or 3 colors. The logo should reproduce well in black/1 color.

The idea of this design is to convey quality and simplicity, like a "no frills", premium quality brand.

Deliverable: fully editable (text and illustration):

Logo.

Basic Jar label design.

Basic Bag label design.

Target Market(s)

Educated women aged 22-45

Industry/Entity Type

Plastic

Requirements
Must have
• Clear, simple logo, delivered in vector form, 1 color/black.
• Use of logo on 1 jar label and 1 bag label, each with product name and space for required and optional marketing content.
Nice to have
• Additional iterations of the design to demonstrate your concept of how we will visually vary additional items in jars and bags.
• i.e. What an additional product in a bag would look like for purposes of brand consistency and product differentiation on shelf or online in e-store.
Should not have
• overly detailed graphics that don't scale well and/or may be hard to read or understand. 4 color design elements (except to simiulate how the product may look through the clear jar or bag or how the product may be placed in a simulated surrounding or ad.

```html
<!DOCTYPE html>
<html lang="en">
<head>
<meta charset="utf-8">
<title>Penny Harvest – Coconut Oil Jar Label</title>
<link rel="stylesheet" href="https://fonts.googleapis.com/css2?family=Questrial&family=Sniglet&display=swap">
<style>
  :root {
    --page-bg: #ffffff;
    --caption-grey: #8c8c8c;
    --label-brown: #2e1810;
    --label-tan: #c4b59f;
    --leaf-green: #8bc652;
    --text-cream: #ffffff;
    --flourish-tan: #b9a88e;
    --product-light: #f1f2f3;
    --product-shade: #b7bbbf;
  }
  * { margin: 0; padding: 0; box-sizing: border-box; }
  html, body {
    width: 954px;
    height: 1200px;
    overflow: hidden;
    background: var(--page-bg);
  }
  .sheet {
    position: relative;
    width: 954px;
    height: 1200px;
  }
  .panel-caption {
    position: absolute;
    top: 30px;
    width: 410px;
    text-align: center;
    font-family: "Questrial", sans-serif;
    font-size: 24px;
    letter-spacing: 0.5px;
    color: var(--caption-grey);
  }
  .panel-caption--front { left: 45px; }
  .panel-caption--back { left: 504px; }

  .label {
    position: absolute;
    top: 88px;
    width: 410px;
    height: 1063px;
  }
  .label--front { left: 45px; background: var(--label-brown); }
  .label--back { left: 504px; background: var(--label-tan); }

  .brand-name {
    position: absolute;
    top: 205px;
    left: 0;
    width: 100%;
    text-align: center;
    font-family: "Questrial", sans-serif;
    font-size: 64px;
    line-height: 1.05;
    color: var(--text-cream);
  }

  .product-visual {
    position: absolute;
    left: 90px;
    top: 419px;
    width: 266px;
    height: 266px;
    border-radius: 50%;
    background: radial-gradient(circle at 45% 40%, var(--product-light) 0%, #d9dcdf 55%, var(--product-shade) 100%);
  }

  .product-tag {
    position: absolute;
    top: 832px;
    left: 0;
    width: 100%;
    text-align: center;
    font-family: "Sniglet", sans-serif;
    font-size: 30px;
    color: var(--leaf-green);
  }

  .flourish {
    position: absolute;
    left: 144px;
    top: 882px;
    width: 156px;
    height: 30px;
    border-radius: 4px;
    background: var(--flourish-tan);
    opacity: 0.85;
  }

  .product-name {
    position: absolute;
    top: 924px;
    left: 0;
    width: 100%;
    text-align: center;
    font-family: "Questrial", sans-serif;
    font-size: 28px;
    line-height: 40px;
    letter-spacing: 2px;
    color: var(--text-cream);
  }
</style>
</head>
<body>
  <div class="sheet">
    <div class="panel-caption panel-caption--front">FRONT LABEL</div>
    <div class="panel-caption panel-caption--back">BACK LABEL</div>

    <section class="label label--front">
      <h1 class="brand-name">Penny<br>Harvest</h1>
      <div class="product-visual" role="img" aria-label="Photo of white solid coconut oil"></div>
      <p class="product-tag">ORGANIC</p>
      <div class="flourish" role="img" aria-label="Decorative scroll flourish"></div>
      <p class="product-name">COLD PRESSED<br>COCONUT OIL</p>
    </section>

    <section class="label label--back"></section>
  </div>
</body>
</html>
```